Landing page for B2B Product Idea Validation Event

We need a single landing page design for the world’s first competition to help aspiring entrepreneurs to validate their new business 2 business (B2B) web application ideas.

We like the following landing pages as examples for the structure and sectioning we would like to see for this landing page:
http://ny.brelvox-summit.com/
https://kiv.com/kivfest

There should be around 5 sections including an application form.

Target Market(s)

Entrepreneurs

Industry/Entity Type

Business Software

Number of Pages Required

1 page

Font styles to use
Serif

Requirements
Must have
• Colors must be similar to the logo provided.

```html
<!DOCTYPE html>
<html lang="en">
<head>
<meta charset="utf-8">
<title>B2B Idea Validation Competition</title>
<link href="https://fonts.googleapis.com/css2?family=Open+Sans:wght@400;600;700&display=swap" rel="stylesheet">
<style>
:root{
  --blue:#1f6fbf;
  --blue-dark:#173f73;
  --navy-band:rgba(28,52,98,.88);
  --ink:#1d1d1d;
  --muted:#555;
  --field:#e6e6e6;
  --field-line:#d3d3d3;
  --caption:#ececec;
  --dark:#141414;
  --white:#fff;
}
*{box-sizing:border-box;margin:0;padding:0}
html,body{width:1200px;height:3383px;overflow:hidden}
body{font-family:"Open Sans",Arial,sans-serif;color:var(--ink);background:var(--white);position:relative}
.abs{position:absolute}

/* hero */
.hero{left:0;top:0;width:1200px;height:616px;background:linear-gradient(180deg,#4d4f57 0%,#6b6c72 40%,#3a3530 100%)}
.milestone{display:flex;gap:14px;color:var(--white)}
.milestone .cal{width:46px;height:46px;background:var(--blue);display:flex;align-items:center;justify-content:center}
.milestone b{display:block;font-size:17px;font-weight:700;line-height:22px}
.milestone span{font-size:14px;opacity:.85}
.tagline{left:120px;width:960px;top:322px;text-align:center;color:var(--white);font-size:21px;line-height:32px}
.btn{background:var(--blue);color:var(--white);font-weight:700;text-align:center}
.hero-cta{left:526px;top:408px;width:170px;height:38px;line-height:38px;font-size:17px}

/* features */
.tile{background:var(--caption)}
.tile .ph{width:100%}
.tile p{font-size:12.5px;font-weight:600;text-align:center;line-height:16px;padding:6px 10px;color:#333}
.tile .cap{display:flex;align-items:center;justify-content:center}

/* headings */
.sec-title{left:0;width:1200px;text-align:center;font-size:30px;font-weight:700}
.sec-title em{font-style:normal;color:var(--blue)}
.ornament{left:390px;width:420px;height:20px}

/* process */
.process{left:0;top:1173px;width:1200px;height:413px;background:linear-gradient(180deg,#2b2722,#1a1815)}
.step-text{width:220px;text-align:center;color:var(--white);font-size:14px;font-weight:700;line-height:20px}

/* judges */
.judge{width:230px;height:214px;overflow:hidden}
.judge .name{position:absolute;left:0;bottom:0;width:100%;height:40px;line-height:40px;background:var(--navy-band);color:var(--white);text-align:center;font-size:15px;font-weight:700}
.judge.active{background:#4a5e86}
.judge.active .info{position:absolute;inset:0;background:var(--navy-band);color:var(--white);text-align:center;padding:28px 16px}
.judge.active h4{font-size:15px;margin-bottom:8px}
.judge.active p{font-size:12.5px;line-height:18px}
.socials{display:flex;justify-content:center;gap:10px;margin-top:12px}
.socials i{width:22px;height:22px;border:1.5px solid var(--white);border-radius:50%}

/* prize */
.prize{left:0;top:2211px;width:1200px;height:444px;background:var(--dark)}
.perk{display:flex;align-items:center;gap:16px;color:var(--white);font-size:15.5px}

/* form */
.field{background:var(--field);border:1px solid var(--field-line);font-size:13px;color:#555;padding:0 12px;display:flex;align-items:center}
.gender{font-size:13px;color:#555;display:flex;align-items:center;gap:10px}
.box{width:13px;height:13px;border:1px solid #888;background:var(--white);display:inline-block;vertical-align:middle;margin-right:6px}
.questions-label{left:99px;top:2886px;font-size:30px;color:var(--blue)}
.q{background:var(--field);border:1px solid var(--field-line);font-size:13px;color:#444;padding:10px 12px;line-height:24px}
.footer{left:0;top:3287px;width:1200px;height:96px;background:var(--dark);color:#ddd}
.footer small{position:absolute;left:99px;top:38px;font-size:13px}
.footer .brand{position:absolute;right:99px;top:26px;font-size:30px;font-weight:600;color:#d8d8d8;display:flex;align-items:center;gap:12px}
.footer .brand i{width:16px;height:16px;background:#d8d8d8;border-radius:50%}
</style>
</head>
<body>

<section class="hero abs" role="img" aria-label="Photo: business team meeting around a boardroom table with a chart on a screen"></section>
<div class="milestone abs" style="left:99px;top:70px">
  <div class="cal"><svg width="20" height="20" viewBox="0 0 20 20"><rect x="2" y="4" width="16" height="14" fill="none" stroke="#fff" stroke-width="2"/><line x1="2" y1="8" x2="18" y2="8" stroke="#fff" stroke-width="2"/><line x1="6" y1="2" x2="6" y2="6" stroke="#fff" stroke-width="2"/><line x1="14" y1="2" x2="14" y2="6" stroke="#fff" stroke-width="2"/></svg></div>
  <div><b>Open Submissions</b><span>Early August</span></div>
</div>
<div class="milestone abs" style="left:801px;top:70px">
  <div class="cal"><svg width="20" height="20" viewBox="0 0 20 20"><rect x="2" y="4" width="16" height="14" fill="none" stroke="#fff" stroke-width="2"/><line x1="2" y1="8" x2="18" y2="8" stroke="#fff" stroke-width="2"/><line x1="6" y1="2" x2="6" y2="6" stroke="#fff" stroke-width="2"/><line x1="14" y1="2" x2="14" y2="6" stroke="#fff" stroke-width="2"/></svg></div>
  <div><b>Close Round 1 Submissions</b><span>September 16th</span></div>
</div>
<p class="tagline abs">The world's first competition to help aspiring entrepreneurs to validate their new business 2 business (B2B) ideas</p>
<div class="btn hero-cta abs">Start Differently</div>

<!-- feature grid -->
<div class="tile abs" style="left:99px;top:661px;width:316px;height:472px">
  <div class="ph" style="height:411px;background:linear-gradient(135deg,#a0764c,#5a3d26)" role="img" aria-label="Photo: hands typing on a laptop on a wooden desk"></div>
  <div class="cap" style="height:61px"><p>Passionate Individual</p></div>
</div>
<div class="tile abs" style="left:433px;top:661px;width:395px;height:223px">
  <div class="ph" style="height:156px;background:linear-gradient(135deg,#8a9bb2,#4b5a70)" role="img" aria-label="Photo: team collaborating around a table"></div>
  <div class="cap" style="height:67px"><p>Your Idea Is B2b Solution (aka Selling To Other Businesses)</p></div>
</div>
<div class="tile abs" style="left:433px;top:907px;width:190px;height:226px">
  <div class="ph" style="height:160px;background:linear-gradient(135deg,#9aa7b5,#3f4b5a)" role="img" aria-label="Photo: man working at a computer"></div>
  <div class="cap" style="height:66px"><p>Your Idea If Validated Would Be A SaaS Product/company</p></div>
</div>
<div class="tile abs" style="left:638px;top:907px;width:190px;height:226px">
  <div class="ph" style="height:160px;background:linear-gradient(135deg,#a8734e,#3e3a44)" role="img" aria-label="Photo: mentoring session in a meeting room"></div>
  <div class="cap" style="height:66px"><p>You Seek Coaching And Mentoring To Help Validate Your Idea</p></div>
</div>
<div class="tile abs" style="left:844px;top:661px;width:257px;height:472px">
  <div class="ph" style="height:350px;background:linear-gradient(135deg,#e6e9ec,#8f9296)" role="img" aria-label="Photo: businessman looking at a monitor in a bright office"></div>
  <div class="cap" style="height:122px"><p>You Currently Have Visibility Or Directly Involved With A Problem In Your Industry</p></div>
</div>

<!-- process -->
<section class="process abs" role="img" aria-label="Background photo: planning sketches and a laptop on a desk"></section>
<h2 class="sec-title abs" style="top:1212px;color:var(--white)">Application and Review Process</h2>
<svg class="ornament abs" style="top:1260px" viewBox="0 0 420 20"><line x1="0" y1="10" x2="190" y2="10" stroke="#bbb"/><line x1="230" y1="10" x2="420" y2="10" stroke="#bbb"/><path d="M200 10 L210 4 L220 10 L210 16Z" fill="#ccc"/></svg>
<svg class="abs" style="left:0;top:1173px" width="1200" height="413" viewBox="0 0 1200 413">
  <g fill="none" stroke="#888" stroke-dasharray="2 6"><line x1="265" y1="219" x2="380" y2="219"/><line x1="540" y1="219" x2="655" y2="219"/><line x1="815" y1="219" x2="930" y2="219"/></g>
  <g>
    <g transform="translate(185,219)">
      <path d="M0 -80 A80 80 0 0 1 80 0" stroke="#fff" stroke-width="3" fill="none"/><path d="M74 -6 L80 8 L86 -6Z" fill="#fff"/>
      <circle r="64" fill="#0f2f63"/><circle r="56" fill="#1f6fbf" stroke="#fff" stroke-width="3"/>
      <rect x="-20" y="-16" width="32" height="32" fill="none" stroke="#fff" stroke-width="4"/><path d="M-4 4 L18 -18" stroke="#fff" stroke-width="5"/>
      <circle cx="-62" cy="57" r="17" fill="#fff"/><text x="-62" y="62" font-size="14" text-anchor="middle" fill="#222" font-family="Open Sans,sans-serif">01</text>
    </g>
    <g transform="translate(458,219)">
      <path d="M0 -80 A80 80 0 0 1 80 0" stroke="#fff" stroke-width="3" fill="none"/><path d="M74 -6 L80 8 L86 -6Z" fill="#fff"/>
      <circle r="64" fill="#0f2f63"/><circle r="56" fill="#1f6fbf" stroke="#fff" stroke-width="3"/>
      <path d="M-20 -18 L6 0 L-20 18Z" fill="#fff"/><rect x="10" y="-18" width="8" height="36" fill="#fff"/>
      <circle cx="-62" cy="-57" r="17" fill="#fff"/><text x="-62" y="-52" font-size="14" text-anchor="middle" fill="#222" font-family="Open Sans,sans-serif">02</text>
    </g>
    <g transform="translate(733,219)">
      <path d="M0 -80 A80 80 0 0 1 80 0" stroke="#fff" stroke-width="3" fill="none"/><path d="M74 -6 L80 8 L86 -6Z" fill="#fff"/>
      <circle r="64" fill="#0f2f63"/><circle r="56" fill="#1f6fbf" stroke="#fff" stroke-width="3"/>
      <rect x="-16" y="-22" width="30" height="42" fill="#fff"/><g stroke="#1f6fbf" stroke-width="3"><line x1="-10" y1="-12" x2="8" y2="-12"/><line x1="-10" y1="-2" x2="8" y2="-2"/><line x1="-10" y1="8" x2="4" y2="8"/></g>
      <circle cx="-62" cy="57" r="17" fill="#fff"/><text x="-62" y="62" font-size="14" text-anchor="middle" fill="#222" font-family="Open Sans,sans-serif">03</text>
    </g>
    <g transform="translate(1006,219)">
      <path d="M0 -80 A80 80 0 0 1 80 0" stroke="#fff" stroke-width="3" fill="none"/><path d="M74 -6 L80 8 L86 -6Z" fill="#fff"/>
      <circle r="64" fill="#0f2f63"/><circle r="56" fill="#1f6fbf" stroke="#fff" stroke-width="3"/>
      <circle cy="-8" r="14" fill="none" stroke="#fff" stroke-width="3"/><rect x="-5" y="-10" width="10" height="32" rx="5" fill="#fff"/>
      <circle cx="-62" cy="-57" r="17" fill="#fff"/><text x="-62" y="-52" font-size="14" text-anchor="middle" fill="#222" font-family="Open Sans,sans-serif">04</text>
    </g>
  </g>
</svg>
<p class="step-text abs" style="left:75px;top:1486px">Submissions Will Be Reviewed By A Round 1 Judging Committee</p>
<p class="step-text abs" style="left:348px;top:1486px">Initial Judging Will Limit The Field To 20 Ideas</p>
<p class="step-text abs" style="left:623px;top:1486px">These 20 ideas will be asked to submit 10 minute pitch video on their idea</p>
<p class="step-text abs" style="left:896px;top:1486px">These videos will be reviewed round 2 judges they will select 10 winners</p>

<!-- judges -->
<h2 class="sec-title abs" style="top:1623px">Judges/<em>Mentors</em></h2>
<svg class="ornament abs" style="top:1671px" viewBox="0 0 420 20"><line x1="0" y1="10" x2="190" y2="10" stroke="#bbb"/><line x1="230" y1="10" x2="420" y2="10" stroke="#bbb"/><path d="M200 10 L210 4 L220 10 L210 16Z" fill="#444"/></svg>

<div class="judge active abs" style="left:99px;top:1717px" role="img" aria-label="Portrait photo of judge">
  <div class="info"><h4>RENDAL OKAFOR</h4><p>Serial founder and B2B advisor who helps early teams test ideas with real buyers.</p><div class="socials"><i></i><i></i><i></i></div></div>
</div>
<div class="judge abs" style="left:356px;top:1717px;background:linear-gradient(160deg,#8b6b52,#d8b99a)" role="img" aria-label="Portrait photo of judge"><div class="name">BRAM WELLER</div></div>
<div class="judge abs" style="left:614px;top:1717px;background:linear-gradient(160deg,#5b5d62,#c9b6a4)" role="img" aria-label="Portrait photo of judge"><div class="name">NOEL DRESDEN</div></div>
<div class="judge abs" style="left:871px;top:1717px;background:linear-gradient(160deg,#6d6f74,#4a3426)" role="img" aria-label="Portrait photo of judge"><div class="name">JALEN PARDO</div></div>
<div class="judge abs" style="left:228px;top:1956px;background:linear-gradient(160deg,#3a3a40,#b58e78)" role="img" aria-label="Portrait photo of judge"><div class="name">JANELLE SORVIK</div></div>
<div class="judge abs" style="left:485px;top:1956px;background:linear-gradient(160deg,#8e8e8e,#c9a48a)" role="img" aria-label="Portrait photo of judge"><div class="name">JONAS KREMER</div></div>
<div class="judge abs" style="left:742px;top:1956px;background:linear-gradient(160deg,#a6a6a0,#b88a6c)" role="img" aria-label="Portrait photo of judge"><div class="name">MILO JARVIE</div></div>

<!-- prize -->
<section class="prize abs" role="img" aria-label="Dark background photo of a celebrating crowd"></section>
<h2 class="sec-title abs" style="top:2250px;color:var(--white)">Our Prize</h2>
<svg class="ornament abs" style="top:2296px" viewBox="0 0 420 20"><line x1="0" y1="10" x2="190" y2="10" stroke="#999"/><line x1="230" y1="10" x2="420" y2="10" stroke="#999"/><path d="M200 10 L210 4 L220 10 L210 16Z" fill="#ccc"/></svg>
<div class="perk abs" style="left:104px;top:2352px"><svg width="18" height="18"><rect x="1" y="3" width="14" height="14" fill="none" stroke="#fff" stroke-width="1.5"/><path d="M4 9 L8 13 L17 2" fill="none" stroke="#fff" stroke-width="2.5"/></svg>Proven Guided Validation Process on your idea with industry experts</div>
<div class="perk abs" style="left:104px;top:2395px"><svg width="18" height="18"><rect x="1" y="3" width="14" height="14" fill="none" stroke="#fff" stroke-width="1.5"/><path d="M4 9 L8 13 L17 2" fill="none" stroke="#fff" stroke-width="2.5"/></svg>Step by Step Process and tools to validate your idea (aka our coaching model)</div>
<div class="perk abs" style="left:104px;top:2438px"><svg width="18" height="18"><rect x="1" y="3" width="14" height="14" fill="none" stroke="#fff" stroke-width="1.5"/><path d="M4 9 L8 13 L17 2" fill="none" stroke="#fff" stroke-width="2.5"/></svg>Insider tips and tricks for success</div>
<div class="perk abs" style="left:104px;top:2481px"><svg width="18" height="18"><rect x="1" y="3" width="14" height="14" fill="none" stroke="#fff" stroke-width="1.5"/><path d="M4 9 L8 13 L17 2" fill="none" stroke="#fff" stroke-width="2.5"/></svg>6 week process</div>
<div class="perk abs" style="left:104px;top:2524px"><svg width="18" height="18"><rect x="1" y="3" width="14" height="14" fill="none" stroke="#fff" stroke-width="1.5"/><path d="M4 9 L8 13 L17 2" fill="none" stroke="#fff" stroke-width="2.5"/></svg>Accountability</div>
<div class="perk abs" style="left:104px;top:2567px"><svg width="18" height="18"><rect x="1" y="3" width="14" height="14" fill="none" stroke="#fff" stroke-width="1.5"/><path d="M4 9 L8 13 L17 2" fill="none" stroke="#fff" stroke-width="2.5"/></svg>Team Sharing</div>
<div class="perk abs" style="left:435px;top:2481px"><svg width="18" height="18"><rect x="1" y="3" width="14" height="14" fill="none" stroke="#fff" stroke-width="1.5"/><path d="M4 9 L8 13 L17 2" fill="none" stroke="#fff" stroke-width="2.5"/></svg>Coaching from experts</div>
<div class="perk abs" style="left:435px;top:2524px"><svg width="18" height="18"><rect x="1" y="3" width="14" height="14" fill="none" stroke="#fff" stroke-width="1.5"/><path d="M4 9 L8 13 L17 2" fill="none" stroke="#fff" stroke-width="2.5"/></svg>Seed Investor Introductions</div>
<div class="perk abs" style="left:435px;top:2567px"><svg width="18" height="18"><rect x="1" y="3" width="14" height="14" fill="none" stroke="#fff" stroke-width="1.5"/><path d="M4 9 L8 13 L17 2" fill="none" stroke="#fff" stroke-width="2.5"/></svg>Prototype Guidance</div>
<div class="abs" style="left:800px;top:2324px;width:250px;height:282px;border-radius:50%;background:radial-gradient(ellipse at 50% 40%,#f2cf5b 0%,#b8861f 45%,rgba(20,20,20,0) 72%)" role="img" aria-label="Illustration: golden trophy with a ribbon banner"></div>

<!-- form -->
<h2 class="sec-title abs" style="top:2692px">Application <em>Form</em></h2>
<svg class="ornament abs" style="top:2740px" viewBox="0 0 420 20"><line x1="0" y1="10" x2="190" y2="10" stroke="#bbb"/><line x1="230" y1="10" x2="420" y2="10" stroke="#bbb"/><path d="M200 10 L210 4 L220 10 L210 16Z" fill="#444"/></svg>
<div class="field abs" style="left:99px;top:2786px;width:325px;height:34px">First Name :</div>
<div class="field abs" style="left:442px;top:2786px;width:321px;height:34px">Last Name :</div>
<div class="field abs" style="left:776px;top:2786px;width:325px;height:34px">Date Of Birth :</div>
<div class="field abs" style="left:99px;top:2834px;width:325px;height:32px">Email :</div>
<div class="field abs" style="left:442px;top:2834px;width:321px;height:32px">Phone No :</div>
<div class="gender abs" style="left:796px;top:2840px">Gender : <span><span class="box"></span>Male</span> <span><span class="box"></span>Female</span></div>
<p class="questions-label abs">Questions :</p>
<div class="q abs" style="left:99px;top:2951px;width:325px;height:68px">Q : 1 Sed ut perspiciatis unde omnis iste ?<br>Ans :</div>
<div class="q abs" style="left:442px;top:2951px;width:321px;height:68px">Q : 2 Sed ut perspiciatis unde omnis iste ?<br>Ans :</div>
<div class="q abs" style="left:776px;top:2951px;width:325px;height:68px">Q : 3 Sed ut perspiciatis unde omnis iste ?<br>Ans :</div>
<div class="q abs" style="left:99px;top:3032px;width:325px;height:68px">Q : 4 Sed ut perspiciatis unde omnis iste ?<br>Ans :</div>
<div class="q abs" style="left:442px;top:3032px;width:321px;height:68px">Q : 5 Sed ut perspiciatis unde omnis iste ?<br>Ans :</div>
<div class="q abs" style="left:776px;top:3032px;width:325px;height:68px">Q : 6 Sed ut perspiciatis unde omnis iste ?<br><span class="box"></span>Yes &nbsp;&nbsp;&nbsp; <span class="box"></span>No</div>
<div class="q abs" style="left:99px;top:3113px;width:1002px;height:68px">Q : 7 Sed ut perspiciatis unde omnis iste natus error sit voluptatem accusantium doloremque laudantium, totam rem aperiam, eaque ipsa ?<br><span class="box"></span>Yes &nbsp;&nbsp;&nbsp; <span class="box"></span>No</div>
<div class="btn abs" style="left:535px;top:3206px;width:128px;height:40px;line-height:40px;font-size:16px">SUBMIT</div>

<footer class="footer abs">
  <small>Copyright © 2016 Leadforge. All Rights Reserved.</small>
  <div class="brand"><i></i>Northbay Labs</div>
</footer>
</body>
</html>
```